Falcrest security business card

Looking for a business card for my security company

Target Market(s)

Security

Industry/Entity Type

Security

Contact Information for Business Card

Name - Gil Marston. Title - General manager - direct 314 862.4490 website www. falcrestsecurityservices.example email - gil@ falcrestsecurityservices.example

Requirements
Must have
• Logo attached

```html
<!DOCTYPE html>
<html lang="en">
<head>
<meta charset="utf-8">
<title>Falcrest Security — Business Card</title>
<link href="https://fonts.googleapis.com/css2?family=Montserrat:wght@400;500;700;800&display=swap" rel="stylesheet">
<style>
  :root {
    --backdrop: #2a2a2a;
    --card: #030303;
    --gold: #c9a046;
    --gold-light: #ecc976;
    --gold-dark: #8c6a24;
    --ink-light: #e8e8e8;
  }
  * { box-sizing: border-box; margin: 0; padding: 0; }
  html, body {
    width: 1200px; height: 1186px; overflow: hidden;
    background: var(--backdrop);
    font-family: "Montserrat", sans-serif;
  }
  .sheet {
    width: 1200px; height: 1186px;
    display: flex; flex-direction: column; align-items: center; justify-content: center;
    gap: 60px;
  }
  .card {
    position: relative;
    width: 900px; height: 500px;
    background: var(--card);
    border-radius: 34px;
    border: 3px solid var(--gold);
    box-shadow: 0 18px 40px rgba(0,0,0,.55);
    overflow: hidden;
  }
  .brand {
    position: absolute;
    display: flex; align-items: center; gap: 18px;
    color: var(--gold);
    font-weight: 800;
    text-transform: uppercase;
    letter-spacing: 2px;
    line-height: 1;
  }
  .brand-mark {
    background: var(--gold);
    flex: none;
  }
  .card-front .brand {
    left: 50%; top: 50%; transform: translate(-50%, -50%);
    font-size: 92px;
  }
  .card-front .brand-mark { width: 40px; height: 40px; }
  .card-back .brand {
    right: 70px; top: 92px;
    font-size: 58px;
  }
  .card-back .brand-mark { width: 26px; height: 26px; }
  .divider {
    position: absolute; height: 2px;
    background: linear-gradient(90deg, var(--gold-light), var(--gold) 50%, var(--gold-dark));
  }
  .divider-top { right: 70px; width: 430px; top: 215px; }
  .divider-contact { left: 60px; right: 70px; top: 392px; }
  .holder {
    position: absolute; left: 60px; top: 292px;
  }
  .holder-name {
    color: var(--gold);
    font-weight: 800; font-size: 42px; letter-spacing: .5px;
  }
  .holder-title {
    color: var(--ink-light);
    font-weight: 500; font-size: 22px; margin-top: 4px;
  }
  .contacts {
    position: absolute; left: 60px; right: 70px; top: 412px;
    display: flex; gap: 70px;
    color: var(--ink-light); font-size: 21px; font-weight: 500;
  }
  .contact { display: flex; align-items: center; gap: 14px; }
  .contact svg { width: 22px; height: 22px; fill: var(--gold); flex: none; }
</style>
</head>
<body>
  <main class="sheet">
    <section class="card card-front">
      <div class="brand"><span class="brand-mark"></span>Falcrest</div>
    </section>

    <section class="card card-back">
      <div class="brand"><span class="brand-mark"></span>Falcrest</div>
      <div class="divider divider-top"></div>

      <div class="holder">
        <p class="holder-name">Gil Marston</p>
        <p class="holder-title">General manager</p>
      </div>
      <div class="divider divider-contact"></div>

      <div class="contacts">
        <p class="contact">
          <svg viewBox="0 0 24 24" aria-hidden="true"><path d="M6.6 10.8a15.1 15.1 0 0 0 6.6 6.6l2.2-2.2c.3-.3.7-.4 1-.2 1.1.4 2.3.6 3.6.6.6 0 1 .4 1 1V20c0 .6-.4 1-1 1C10.6 21 3 13.4 3 4c0-.6.4-1 1-1h3.5c.6 0 1 .4 1 1 0 1.3.2 2.5.6 3.6.1.3 0 .7-.2 1z"/></svg>
          314 862.4490
        </p>
        <p class="contact">
          <svg viewBox="0 0 24 24" aria-hidden="true"><path d="M12 2a10 10 0 1 0 0 20 10 10 0 0 0 0-20zm6.9 6h-2.9a15.6 15.6 0 0 0-1.4-3.6A8 8 0 0 1 18.9 8zM12 4c.8 1.2 1.5 2.5 1.9 4h-3.8c.4-1.5 1.1-2.8 1.9-4zM4.3 14a8 8 0 0 1 0-4h3.4a16 16 0 0 0 0 4zm.8 2h2.9c.3 1.3.8 2.5 1.4 3.6A8 8 0 0 1 5.1 16zM8 8H5.1a8 8 0 0 1 4.3-3.6C8.8 5.5 8.3 6.7 8 8zm4 12c-.8-1.2-1.5-2.5-1.9-4h3.8c-.4 1.5-1.1 2.8-1.9 4zm2.3-6H9.7a14.7 14.7 0 0 1 0-4h4.6a14.7 14.7 0 0 1 0 4zm.3 5.6c.6-1.1 1.1-2.3 1.4-3.6h2.9a8 8 0 0 1-4.3 3.6zm1.7-5.6a16 16 0 0 0 0-4h3.4a8 8 0 0 1 0 4z"/></svg>
          www.falcrestsecurityservices.example
        </p>
      </div>
    </section>
  </main>
</body>
</html>
```